Awesome Beer Labels for food pairing

We are going to launch a range of craft beers specially brewed for food pairing, and we are in need of a logo and bottle labels to represent this. Every label individually has to show which beer type it is and the food groups it matches with. At the same time the whole range has to have the same appearance as we are promoting it as a whole package. As we are targeting middle-high to high class hospitality businesses we are looking for a luxurious, exclusive feel to the labels. We also need room for a clear title of the beer and a small food pairing description.

Industry/Entity Type

Craft Brewery

Font styles to use
Sans Serif
Decorative
Script

Colors

Designer to choose colors to be used in the design.

Requirements
Must have
• -Different beer labels where the style and name of the beer comes first, and the beer type second
• - A logo for the whole group which also has to be printed on glasses, so nothing to detailed.
• - Clear, recognizable pictures, drawings or symbols for the different food groups.
• - Room for the name of the beer, the beer type and a small description.
Nice to have
• An exclusive, luxurious look and feel that would not stand out in an high class restaurant.
• Something that combines the whole range of beers (something like a overlaying or connecting picture that combines alle the labels?)
Should not have
• To much different styles, the beers have to match

```html
<!DOCTYPE html>
<html lang="en">
<head>
<meta charset="utf-8">
<title>Craft Beer Label</title>
<link rel="stylesheet" href="https://fonts.googleapis.com/css2?family=Lobster&family=Oswald:wght@400;500;700&display=swap">
<style>
  :root {
    --backdrop: #e4e6e8;
    --label-black: #050505;
    --gold: #d9b23c;
    --gold-bright: #f2d46a;
    --gold-pale: #f6ea9c;
    --gold-deep: #6e5614;
    --cheese: #f3bd3a;
    --steak: #a8543c;
  }
  * { margin: 0; padding: 0; box-sizing: border-box; }
  html, body {
    width: 1200px;
    height: 800px;
    overflow: hidden;
    background: var(--backdrop);
  }
  .canvas {
    position: relative;
    width: 1200px;
    height: 800px;
  }
  .label {
    position: absolute;
    left: 340px;
    top: 48px;
    width: 520px;
    height: 704px;
    background: var(--label-black);
    box-shadow: 6px 8px 14px rgba(0,0,0,0.25);
    overflow: hidden;
    font-family: "Oswald", sans-serif;
  }
  .burst {
    position: absolute;
    inset: 0;
    background: radial-gradient(circle at 50% 58%, rgba(120,96,30,0.45) 0%, rgba(70,56,18,0.25) 35%, rgba(5,5,5,0) 70%);
  }
  .brand {
    position: absolute;
    top: 44px;
    left: 0;
    width: 100%;
    display: flex;
    flex-direction: column;
    align-items: center;
    gap: 12px;
  }
  .brand-dot {
    width: 62px;
    height: 62px;
    border-radius: 50%;
    border: 3px solid var(--gold);
  }
  .brand-name {
    font-family: "Oswald", sans-serif;
    font-weight: 500;
    font-size: 24px;
    letter-spacing: 3px;
    color: var(--gold);
    text-transform: uppercase;
  }
  .frame {
    position: absolute;
    left: 75px;
    top: 187px;
    width: 370px;
    height: 445px;
    border: 3px solid var(--gold-bright);
    box-shadow: 0 0 0 1px var(--gold-deep), inset 0 0 0 1px var(--gold-deep);
  }
  .title-script {
    position: absolute;
    top: 196px;
    left: 0;
    width: 100%;
    text-align: center;
    font-family: "Lobster", cursive;
    font-size: 68px;
    line-height: 1;
    color: var(--gold-pale);
    transform: translateX(-8px);
  }
  .title-main {
    position: absolute;
    top: 250px;
    left: 0;
    width: 100%;
    text-align: center;
    font-family: "Oswald", sans-serif;
    font-weight: 700;
    font-size: 172px;
    line-height: 1;
    letter-spacing: -2px;
    color: var(--gold-pale);
    -webkit-text-stroke: 3px var(--gold-deep);
    paint-order: stroke fill;
  }
  .beer-type {
    position: absolute;
    top: 428px;
    left: 0;
    width: 100%;
    text-align: center;
    font-weight: 500;
    font-size: 36px;
    color: var(--gold-pale);
  }
  .pairing-note {
    position: absolute;
    top: 492px;
    left: 100px;
    width: 320px;
    text-align: center;
    font-weight: 400;
    font-size: 12.5px;
    line-height: 1.45;
    color: var(--gold-pale);
  }
  .food-icons {
    position: absolute;
    top: 540px;
    left: 202px;
    width: 120px;
    height: 76px;
    border-radius: 38px;
    background: linear-gradient(90deg, var(--cheese) 0%, var(--cheese) 45%, var(--steak) 55%, var(--steak) 100%);
  }
  .net-volume {
    position: absolute;
    top: 650px;
    left: 0;
    width: 100%;
    text-align: center;
    font-weight: 500;
    font-size: 22px;
    color: var(--gold-pale);
  }
</style>
</head>
<body>
  <main class="canvas">
    <section class="label">
      <div class="burst" role="img" aria-label="Faint gold sunburst rays radiating from the centre of the label"></div>

      <div class="brand">
        <span class="brand-dot"></span>
        <span class="brand-name">Halden Reserve</span>
      </div>

      <div class="frame"></div>

      <p class="title-script">Craft</p>
      <h1 class="title-main">BEER</h1>
      <p class="beer-type">beer type</p>
      <p class="pairing-note">Lorem ipsum dolor sit amet, consectetur adipiscing elit, sed do eiusmod tempor incididunt ut labore et dolore magna .</p>

      <div class="food-icons" role="img" aria-label="Food pairing icons: a wedge of cheese and a grilled steak"></div>

      <p class="net-volume">Nt.Wt. 160 ml</p>
    </section>
  </main>
</body>
</html>
```